Business Card Design for Occupational Medicine Start Up Company

We need to design a professional business card. We are a healthcare company providing occupational medicine services to blue collar industries. We are professional, efficient and high quality service providers.

Target Market(s)

Blue Collar Industry: Shipbuilding, Ports, Trucking Companies; The Executives and Safety Officers for these companies

Industry/Entity Type

Healthcare

Contact Information for Business Card

Logo, Name, Title, Email, Phone

Other font styles liked:
• Please match our Brand Guide

Requirements
Must have
• Our Company Colors and Logo

```html
<!DOCTYPE html>
<html lang="en">
<head>
<meta charset="utf-8">
<title>Crewline Health – Business Card</title>
<link rel="stylesheet" href="https://fonts.googleapis.com/css2?family=Montserrat:wght@600;700&family=Arimo:wght@400;700&display=swap">
<style>
  :root {
    --backdrop: #1d1d1f;
    --navy: #242a7a;
    --navy-deep: #1b2069;
    --sky: #22a3dc;
    --amber: #f3aa45;
    --ink: #333338;
    --paper: #ffffff;
  }
  * { box-sizing: border-box; margin: 0; padding: 0; }
  html, body { width: 1200px; height: 800px; overflow: hidden; }
  body {
    background: var(--backdrop);
    font-family: "Arimo", Arial, sans-serif;
    position: relative;
  }
  .card {
    position: absolute;
    left: 320px;
    width: 560px;
    height: 320px;
    border-radius: 18px;
    overflow: hidden;
  }
  .card--back {
    top: 50px;
    background: linear-gradient(100deg, var(--navy-deep), var(--navy));
    display: flex;
    align-items: center;
    justify-content: center;
  }
  .card--front {
    top: 430px;
    background: var(--paper);
    padding: 44px 0 0 46px;
  }
  .wordmark {
    display: flex;
    align-items: center;
    gap: 12px;
    font-family: "Montserrat", Arial, sans-serif;
    font-weight: 700;
    letter-spacing: 0.02em;
    text-transform: uppercase;
  }
  .wordmark__dot { border-radius: 50%; flex: none; }
  .card--back .wordmark { color: var(--paper); font-size: 40px; }
  .card--back .wordmark__dot { width: 30px; height: 30px; background: var(--amber); }
  .card--front .wordmark { color: var(--navy); font-size: 22px; }
  .card--front .wordmark__dot { width: 16px; height: 16px; background: var(--amber); }
  .holder { margin-top: 26px; }
  .holder__name { font-size: 23px; font-weight: 700; color: var(--navy); }
  .holder__title { font-size: 16px; color: var(--sky); margin-top: 2px; }
  .address { margin-top: 8px; font-size: 14px; line-height: 1.3; color: var(--ink); }
  .contacts { list-style: none; margin-top: 10px; font-size: 14px; line-height: 1.35; color: var(--ink); }
  .contacts li { display: flex; align-items: center; gap: 8px; }
  .contacts svg { width: 12px; height: 12px; flex: none; fill: var(--sky); }
</style>
</head>
<body>
  <section class="card card--back" aria-label="Card back">
    <div class="wordmark"><span class="wordmark__dot"></span>Crewline Health</div>
  </section>

  <section class="card card--front" aria-label="Card front">
    <div class="wordmark"><span class="wordmark__dot"></span>Crewline Health</div>
    <div class="holder">
      <p class="holder__name">Daniel Hart</p>
      <p class="holder__title">President</p>
    </div>
    <p class="address">214 Harbor View Road<br>Kodiak, Alaska 99615</p>
    <ul class="contacts">
      <li><svg viewBox="0 0 12 12"><path d="M2.5 0.8 4.6 3 3.5 4.4c.8 1.6 2.1 3 3.8 3.9L8.7 7l2.5 1.9-1 2.2C5.3 11 1 6.7.9 1.8z"/></svg>555-014-2210</li>
      <li><svg viewBox="0 0 12 12"><path d="M3 0h6v12H3zM4 1.5v8h4v-8z"/></svg>555-014-7784</li>
      <li><svg viewBox="0 0 12 12"><path d="M3 0h5l1 1v3H3zM1 5h10v5H9v2H3v-2H1zM4 9v2h4V9z"/></svg>555-014-3391</li>
      <li><svg viewBox="0 0 12 12"><path d="M0 2h12v8H0zM1 3l5 3.5L11 3v-.2H1z"/></svg>hello@crewlinehealth.com</li>
      <li><svg viewBox="0 0 12 12"><circle cx="6" cy="6" r="6"/></svg>www.crewlinehealth.com</li>
    </ul>
  </section>
</body>
</html>
```